TOLO Electrical Services Letter Head

I need a professional clean looking design that will incorporate my company logo and information such as postal address, website, contact email "service@tolovoltworks.com.au" and phone number.

somewhere on the document i will also require my electrical contractor number "EC 046215" and my Australian Business number "57 139 604 282" these have to legally be on the document so they dont need to be a main feature, maybe in the footer in a smaller text.

Can you also have the 3 blue dashes from my logo as the watermark.

I would like the colour scheme to match my logo, business card and website www.tolovoltworks.com.au

I have the JPEG and PNG files for my logo which it will not allow me to upload as they are too wide, if you require these please let me know.

Target Market(s)

To be used for quotes and letters to commercial clients

Industry/Entity Type

Electric Company

Colors
0555a3
3176b5
85acd3
cfdfed
eaf1f7

Requirements
Must have
• company logo and information such as postal address, website, contact email "service@tolovoltworks.com.au" and phone number.
• somewhere on the document i will also require my electrical contractor number "EC 046215" and my Australian Business number "57 139 604 282" these have to legally be on the document so they dont need to be a main feature, maybe in the footer in a smaller text.
• I would like the colour scheme to match my logo, business card and website www.tolovoltworks.com.au
Nice to have
• Can you also have the 3 blue dashes from my logo as the watermark.

```html
<!DOCTYPE html>
<html lang="en">
<head>
<meta charset="utf-8">
<title>TOLO Electrical Services Letterhead</title>
<link href="https://fonts.googleapis.com/css2?family=Didact+Gothic&display=swap" rel="stylesheet">
<style>
  :root{
    --blue-deep:#0555a3;
    --blue:#3176b5;
    --blue-soft:#85acd3;
    --blue-pale:#cfdfed;
    --blue-mist:#eaf1f7;
    --ink:#2b2b2d;
    --band:#2e2e30;
    --backdrop:#e9e9ea;
    --paper:#ffffff;
  }
  *{box-sizing:border-box;margin:0;padding:0}
  html,body{width:1200px;height:968px;overflow:hidden}
  body{background:var(--backdrop);font-family:"Didact Gothic",sans-serif;color:var(--ink)}
  .letterhead{
    position:absolute;left:282px;top:34px;width:636px;height:900px;
    background:var(--paper);box-shadow:0 2px 10px rgba(0,0,0,.12);overflow:hidden;
  }
  .brand{position:absolute;left:52px;top:62px;display:flex;align-items:center;gap:8px}
  .brand-square{width:14px;height:14px;background:var(--blue)}
  .brand-name{font-size:17px;color:var(--band);letter-spacing:.3px}
  .contact{position:absolute;left:420px;top:52px;font-size:7.5px;line-height:11px;color:#555}
  .contact li{list-style:none;display:flex;align-items:center;gap:5px}
  .contact svg{width:8px;height:8px;flex:none}
  .contact .postal{padding-left:13px}
  .recipient{position:absolute;left:52px;top:200px;font-size:8px;line-height:11.5px}
  .recipient .date{margin-bottom:4px}
  .body{position:absolute;left:108px;top:282px;width:440px;font-size:8px;line-height:11px;text-align:justify}
  .body .salutation{font-weight:bold;margin-bottom:12px}
  .body p{margin-bottom:10px}
  .signoff{position:absolute;left:108px;top:594px;font-size:8px;line-height:11px}
  .signoff strong{display:block}
  .signature{position:absolute;left:200px;top:562px;width:110px;height:54px;background:var(--blue-mist);border-radius:4px}
  .watermark{position:absolute;right:70px;top:560px;width:150px;height:150px;background:var(--blue-mist);opacity:.6}
  .footer-band{position:absolute;left:0;bottom:0;width:100%;height:18px;background:var(--band);display:flex;align-items:center;padding-left:24px}
  .footer-band .legal{font-size:6.5px;color:#fff;letter-spacing:.2px}
  .footer-mark{position:absolute;right:96px;bottom:4px;width:10px;height:10px;background:var(--blue)}
</style>
</head>
<body>
<main class="letterhead">
  <header>
    <div class="brand"><span class="brand-square"></span><span class="brand-name">TOLO Electrical Services</span></div>
    <ul class="contact">
      <li><svg viewBox="0 0 8 8"><rect width="8" height="8" fill="#3176b5"/><path d="M2 1.5l1 1-.6.8a4 4 0 0 0 2.3 2.3l.8-.6 1 1-.8.8C3.5 6.5 1.5 4.5 1.2 2.3z" fill="#fff"/></svg>(08) 6210 4479</li>
      <li><svg viewBox="0 0 8 8"><rect width="8" height="8" fill="#3176b5"/><path d="M1.5 2.5h5v3h-5zM1.5 2.5 4 4.5l2.5-2" fill="none" stroke="#fff" stroke-width=".6"/></svg>service@tolovoltworks.com.au</li>
      <li><svg viewBox="0 0 8 8"><rect width="8" height="8" fill="#3176b5"/><circle cx="4" cy="4" r="2.3" fill="none" stroke="#fff" stroke-width=".6"/><path d="M1.7 4h4.6M4 1.7v4.6" stroke="#fff" stroke-width=".5"/></svg>www.tolovoltworks.com.au</li>
      <li class="postal">P.O Box 7318</li>
      <li class="postal">Harlow Ridge, WA 6178</li>
    </ul>
  </header>

  <section class="recipient">
    <div class="date">30.09.2016</div>
    <div>Recipient's name</div>
    <div>Elmstr. 22</div>
    <div>10115 Musterstadt</div>
    <div>Germany</div>
  </section>

  <div class="watermark" aria-hidden="true"></div>

  <article class="body">
    <div class="salutation">Dear sir,</div>
    <p>Communication is a very integral part of living creatures, animals and humans. Communication may be verbal or written. Written communication however is only applicable to human beings. Can you even imagine a world without communication? Verbal communication can be through telephones, webcams or in person. Written communication is through letters, emails and mobile phone messages.</p>
    <p>In today's world of great inventions and technology, letters have somehow become redundant. It is the time for text messages or chats. But they still can communicate a lot more than all other modes of communication. Organizations and various government departments still bank on letters as a strong medium of communication. There is no comparison in costs of sending letters as compared to costs of mobile phone messages though. Letters are far cheaper. Letters now commonly known as "hard copy documents" are considered more relevant and important than email copies of text messages as proof or evidence of some sort.</p>
    <p>Letters speak volumes about a person or an organization that writes it. So one must take utmost care ensuring that the language used in any letter is appropriate for the occasion for which it is being written. Since a letter is also a written proof or document, there are certain things that should not form a part of it, then that too should be carefully handled.</p>
    <p>Writing a good letter is an art. But if for some reason someone is unable to write that perfect letter, these different types of letters provide a base for you to build on. Sample letters have been given for everyone to understand what all information needs to form a part of the letter type and then it can be customized.</p>
  </article>

  <div class="signature" role="img" aria-label="Handwritten signature of Lena Corrow"></div>
  <div class="signoff">Yours Sincerely,<strong>Lena Corrow</strong></div>

  <footer class="footer-band">
    <span class="legal">EC 046215 / Australian Business number: 57 139 604 282</span>
  </footer>
  <span class="footer-mark" aria-hidden="true"></span>
</main>
</body>
</html>
```